Structural Engineering Firm Looking for High-Impact Lead Generation Focused Design (for B2B)

A well-established structural engineering firm in the UK wants a new website designed for them which will help them realise more business from online. Directly through the website as well as Ads and lead platforms. They need to compare favourably to competitors and have clarity. Current Site is here: http://www.quarlingpartners.example/ - you can take imagery from this site if you want to help with the design.

Target Market(s)

Homeowners, Architects, Designers, Construction Companies and Landlords

Industry/Entity Type

Professional Services

Number of Pages Required

5+ page

Font styles to use
Sans Serif

Requirements
Must have
• A Strong, Simple and Professional Design with a Focus on Lead Generation
Nice to have
• Creativity in the Detail, Clear Messaging
Should not have
• Too Much Colour, Too 'Consumer', Too Much Variation

```html
<!DOCTYPE html>
<html lang="en">
<head>
<meta charset="utf-8">
<title>Quarling Partners – Homepage Design</title>
<link href="https://fonts.googleapis.com/css2?family=Montserrat:wght@600;700&family=Mulish:wght@400;600&display=swap" rel="stylesheet">
<style>
:root{
  --ink:#2b2b2b;
  --teal:#009b9d;
  --mist:#eeeeee;
  --board:#eaeaea;
  --white:#ffffff;
  --grey:#8a8a8a;
  --line:#dcdcdc;
  --pale-teal:#d9efef;
}
*{box-sizing:border-box;margin:0;padding:0}
html,body{width:1200px;height:3748px;overflow:hidden}
body{background:var(--board);font-family:"Mulish",sans-serif;color:var(--ink);position:relative}
.abs{position:absolute}
.head{font-family:"Montserrat",sans-serif;font-weight:700;text-transform:uppercase;color:var(--ink)}
.body-copy{font-size:6.5px;line-height:12px;color:#666}
.body-copy a{color:var(--teal);text-decoration:underline}

/* brand strip */
.brand-name{left:291px;top:108px;font-size:24px;line-height:25px;font-weight:400;color:var(--ink);letter-spacing:.5px}
.strip-rule{width:1px;height:80px;background:#cfcfcf;top:95px}
.strip-label{font-size:20px;color:var(--ink)}
.font-list{font-size:14px;line-height:23px;color:#666}
.swatch{width:38px;height:38px;border-radius:50%;top:122px}
.swatch-code{font-size:8px;color:#777;top:167px}

.device-area{left:120px;top:247px;width:960px;height:517px;border-radius:6px;background:linear-gradient(180deg,#dcdcdc,#e6e6e6)}

/* page */
.page{left:291px;top:826px;width:617px;height:2869px;background:var(--white)}
.logo{left:316px;top:846px;font-size:14px;line-height:13px;color:var(--ink)}
.toplinks{right:316px;top:846px;font-size:5.5px;color:#888;word-spacing:3px}
.nav{right:316px;top:868px;font-size:5.5px;color:var(--ink);word-spacing:18px;letter-spacing:.2px}
.hero{left:316px;top:889px;width:568px;height:299px;background:linear-gradient(180deg,#9aa3aa 0%,#8b7a70 45%,#5a5650 100%)}
.hero-text{left:316px;width:568px;top:983px;text-align:center;font-family:"Montserrat",sans-serif;font-weight:700;font-size:19px;line-height:29px;color:var(--white);text-transform:uppercase}
.hero-text .accent{color:var(--teal)}
.hero-sub{left:316px;width:568px;top:1110px;text-align:center;font-size:6.5px;color:var(--white);letter-spacing:.5px}
.hero-select{left:493px;top:1131px;width:214px;height:24px;border:1px solid rgba(255,255,255,.6);color:#eee;font-size:6px;padding:8px 10px}
.hero-select:after{content:"";position:absolute;right:10px;top:10px;border:3px solid transparent;border-top-color:#fff}

.h2{font-size:13px;line-height:19px}
.photo{background:linear-gradient(160deg,#c7c2b8,#8e8474)}
.frame{border:4px solid var(--pale-teal)}
.divider{height:1px;background:var(--line)}

.band{left:291px;width:617px;background:#f2f2f2}
.btn{background:var(--teal);color:var(--white);font-family:"Montserrat",sans-serif;font-weight:700;font-size:5.5px;text-transform:uppercase;text-align:center;letter-spacing:.3px}
.btn-outline{border:1px solid var(--teal);color:var(--teal);background:var(--white)}
.step{top:1868px;width:132px;height:170px;background:linear-gradient(180deg,#e6e6e6,#9c9c9c)}
.step span{position:absolute;bottom:12px;width:100%;text-align:center;font-family:"Montserrat",sans-serif;font-weight:700;font-size:6px;color:var(--white)}

.field{border:1px solid var(--line);height:24px;font-size:5.5px;color:var(--teal);padding:8px 10px}
.news-img{top:2726px;width:108px;height:129px;background:linear-gradient(160deg,#e9e9e9,#9aa0a3)}
.news-cap{top:2869px;font-size:6.5px;color:#666}
.news-arrow{top:2882px}
.map{background:linear-gradient(160deg,#b8aa98,#6c6358)}
.addr{font-size:6.5px;line-height:12.5px;color:#888}
.addr b{color:var(--ink);font-weight:600}

.foot{left:291px;top:3447px;width:617px;height:248px;background:#f2f2f2}
.foot-col{top:3486px;font-size:8px;color:#555}
.foot-col ul{list-style:none;margin-top:10px}
.foot-col li{font-size:5.5px;line-height:12px;color:#999}
.foot-rule{left:375px;top:3604px;width:451px;height:1px;background:var(--line)}
.foot-base{top:3612px;font-size:5px;color:#999}
</style>
</head>
<body>

<!-- brand strip -->
<div class="abs brand-name">QUARLING<br>PARTNERS</div>
<div class="abs strip-rule" style="left:500px"></div>
<div class="abs strip-label" style="left:560px;top:92px">Fonts:</div>
<div class="abs font-list" style="left:560px;top:134px">Proxima Nova<br>Helvetica Neue</div>
<div class="abs strip-rule" style="left:718px"></div>
<div class="abs strip-label" style="left:778px;top:92px">Colors:</div>
<div class="abs swatch" style="left:779px;background:var(--ink)"></div>
<div class="abs swatch" style="left:826px;background:var(--teal)"></div>
<div class="abs swatch" style="left:873px;background:var(--mist);border:1px solid #e2e2e2"></div>
<div class="abs swatch-code" style="left:780px">#2b2b2b</div>
<div class="abs swatch-code" style="left:827px">#009b9d</div>
<div class="abs swatch-code" style="left:874px">#eeeeee</div>

<div class="abs device-area" role="img" aria-label="Homepage shown on desktop and laptop screens"></div>

<!-- page -->
<div class="abs page"></div>
<div class="abs logo">QUARLING<br>PARTNERS</div>
<div class="abs toplinks">Gallery | Blog | About Us | Contact Us</div>
<div class="abs nav">STRUCTURAL&nbsp;DESIGN STRUCTURAL&nbsp;SURVEYS PLANNING PARTY&nbsp;WALL PARTNERS</div>

<div class="abs hero" role="img" aria-label="Photo of a modern house extension on a brick semi-detached home"></div>
<div class="abs hero-text"><span class="accent">Efficient &amp; Professional</span><br>Structural Engineering<br>&amp; Party Wall Surveying</div>
<div class="abs hero-sub">GET A COMPETITIVE QUOTE FROM THE LOCAL EXPERTS</div>
<div class="abs hero-select">What service are you looking for?</div>

<!-- structural engineers -->
<div class="abs head h2" style="left:375px;top:1256px">Structural Engineers<br>in London and South East</div>
<p class="abs body-copy" style="left:375px;top:1300px;width:222px">If you're looking for structural engineering advice or calculations, then you should talk to Quarling Partners. Whether a <a>basement</a>, <a>extension</a>, <a>loft</a> or any other significant <a>conversion</a> to your home, we're here to help. Or perhaps you just want <a>planning reports</a> or advice on <a>existing designs</a>?</p>
<p class="abs body-copy" style="left:375px;top:1360px;width:222px">Operating out of London and Sussex, we reach all the home counties and can provide you with a very quick appraisal and quote for the calculations and drawings.</p>
<div class="abs frame" style="left:647px;top:1250px;width:185px;height:216px"></div>
<div class="abs photo" style="left:633px;top:1258px;width:192px;height:201px" role="img" aria-label="Photo of a rear house extension with large glazing"></div>

<div class="abs divider" style="left:375px;top:1495px;width:451px"></div>

<!-- party wall -->
<div class="abs frame" style="left:367px;top:1528px;width:72px;height:216px;border-right:none"></div>
<div class="abs photo" style="left:375px;top:1536px;width:192px;height:201px;background:linear-gradient(160deg,#f1f1f1,#b9b9b9)" role="img" aria-label="Photo of a bright interior with a glazed partition"></div>
<div class="abs head h2" style="left:607px;top:1534px">Choose the<br>Party Wall Specialists</div>
<p class="abs body-copy" style="left:607px;top:1578px;width:222px">Where there's a wall, there's a way. And we do more party wall awards than most surveyors. Whether it is part of a <a>planning application</a>, or <a>serving</a> or <a>forming</a> a party wall award, you can lean on us to help guide you.</p>
<p class="abs body-copy" style="left:607px;top:1626px;width:222px">Our experience makes us very adaptable business to your needs. From <a>minor residential works</a> to major projects, we can work directly with you or be a part of your preferred design team.</p>
<p class="abs body-copy" style="left:607px;top:1668px;width:222px">Simply call +44 (0) 1632 960 417 for outside of London, or +44 (0) 20 7946 0302 within the capital, and we can get to work for you.</p>

<!-- steps band -->
<div class="abs band" style="top:1775px;height:302px"></div>
<div class="abs head h2" style="left:316px;top:1812px">From drawing to delivered.<br>We support you every step.</div>
<div class="abs btn" style="left:822px;top:1818px;width:62px;height:22px;line-height:22px">Find out more</div>
<div class="abs step" style="left:316px" role="img" aria-label="Photo of a pen on a design brief"><span>01 - BRIEF</span></div>
<div class="abs step" style="left:461px" role="img" aria-label="Photo of hands reviewing plans"><span>02 - DESIGN</span></div>
<div class="abs step" style="left:606px" role="img" aria-label="Photo of a hand sketching a building"><span>03 - REFINE</span></div>
<div class="abs step" style="left:752px" role="img" aria-label="Photo of a finished architectural model"><span>04 - DELIVER</span></div>

<!-- fast turnaround -->
<div class="abs head h2" style="left:375px;top:2113px">Need a fast turnaround?</div>
<p class="abs body-copy" style="left:375px;top:2140px;width:222px">If your project is in South East of England, we can provide a fast turnaround if needed. Simply tell us the scope of work and provide an address and we can give you an indicative price and book a site visit.</p>
<div class="abs field" style="left:375px;top:2192px;width:220px">What service are you looking for?</div>
<p class="abs body-copy" style="left:375px;top:2228px;width:222px">The Quarling team will be on hand to help you through the process - from brief to calculations to delivery. Simply call 01632 960 417 or <a>book a visit</a> using our form.</p>
<div class="abs frame" style="left:760px;top:2109px;width:72px;height:216px;border-left:none"></div>
<div class="abs photo" style="left:633px;top:2109px;width:142px;height:207px;background:linear-gradient(180deg,#f4f4f4,#c9c9c9)" role="img" aria-label="Photo of a hand holding a stopwatch"></div>
<div class="abs btn" style="left:700px;top:2276px;width:48px;height:20px;line-height:20px">Book a visit</div>

<!-- partnership -->
<div class="abs" style="left:316px;top:2355px;width:568px;height:295px;background:#eeeeee"></div>
<svg class="abs" style="left:316px;top:2355px" width="360" height="295" role="img" aria-label="Photo of engineers in hard hats reviewing plans on site"><defs><linearGradient id="siteTone" x1="0" y1="0" x2="1" y2="1"><stop offset="0" stop-color="#b9c1c7"/><stop offset="1" stop-color="#6f7b6a"/></linearGradient></defs><polygon points="0,0 355,0 260,295 0,295" fill="url(#siteTone)"/></svg>
<div class="abs head h2" style="left:663px;top:2405px">We work in partnership</div>
<p class="abs body-copy" style="left:663px;top:2432px;width:200px">We are familiar in working closely with architects, developers, builders and surveyors on a wide range of projects.</p>
<p class="abs body-copy" style="left:663px;top:2486px">If you would like to explore partnering with Quarling:</p>
<div class="abs btn btn-outline" style="left:663px;top:2513px;width:64px;height:22px;line-height:20px">Find out more</div>
<p class="abs body-copy" style="left:663px;top:2549px">If you would like to explore partnering with Quarling:</p>
<div class="abs btn" style="left:663px;top:2576px;width:116px;height:24px;line-height:24px">Introduce us to your team</div>

<!-- news -->
<div class="abs head h2" style="left:291px;width:617px;top:2686px;text-align:center">News, Events &amp; Features</div>
<div class="abs news-img" style="left:375px" role="img" aria-label="Photo of a glass stair balustrade"></div>
<div class="abs news-img" style="left:489px" role="img" aria-label="Photo of a room with a wide window"></div>
<div class="abs news-img" style="left:603px" role="img" aria-label="Photo of an open-plan kitchen extension"></div>
<div class="abs news-img" style="left:717px" role="img" aria-label="Photo of a dining area under a roof light"></div>
<div class="abs news-cap" style="left:375px">News Headline or Blog story</div>
<div class="abs news-cap" style="left:489px">News Headline or Blog story</div>
<div class="abs news-cap" style="left:603px">News Headline or Blog story</div>
<div class="abs news-cap" style="left:717px">News Headline or Blog story</div>
<svg class="abs news-arrow" style="left:375px" width="10" height="6"><path d="M0 3h8M6 1l2 2-2 2" stroke="#009b9d" fill="none"/></svg>
<svg class="abs news-arrow" style="left:489px" width="10" height="6"><path d="M0 3h8M6 1l2 2-2 2" stroke="#009b9d" fill="none"/></svg>
<svg class="abs news-arrow" style="left:603px" width="10" height="6"><path d="M0 3h8M6 1l2 2-2 2" stroke="#009b9d" fill="none"/></svg>
<svg class="abs news-arrow" style="left:717px" width="10" height="6"><path d="M0 3h8M6 1l2 2-2 2" stroke="#009b9d" fill="none"/></svg>

<!-- offices -->
<div class="abs head h2" style="left:316px;top:3000px">Quarling Partners London</div>
<div class="abs addr" style="left:316px;top:3035px"><b>Main Office</b><br>Studio 4 Wharfside Works<br>12 Larchmont Road<br>London SE1 9ZZ<br>United Kingdom<br><br><b>Tel:</b><br>+44 (0) 20 7946 0302</div>
<div class="abs map" style="left:633px;top:2967px;width:251px;height:200px" role="img" aria-label="Street map of the London office over a photo of the building"></div>

<div class="abs map" style="left:316px;top:3206px;width:251px;height:200px" role="img" aria-label="Street map of the Sussex office over a photo of the building"></div>
<div class="abs head h2" style="left:657px;top:3249px">Quarling Partners Sussex</div>
<div class="abs addr" style="left:657px;top:3282px">Full Street Address<br>Street<br>County<br>Postcode<br><br><b>Tel:</b><br>+44 (0) 1632 960 417</div>

<!-- footer -->
<div class="abs foot"></div>
<div class="abs foot-col" style="left:375px">Design<ul><li>Design Advice</li><li>Lofts</li><li>Steel Beams</li><li>Basements</li><li>House Conversion</li><li>Temporary Works</li></ul></div>
<div class="abs foot-col" style="left:467px">Planning<ul><li>Planning Reports</li><li>Planning Applications</li></ul></div>
<div class="abs foot-col" style="left:567px">Party Wall<ul><li>Serving Party Wall Notices</li><li>Forming Party Wall Awards</li><li>Condition Schedules</li><li>Minor Residential Works</li></ul></div>
<div class="abs foot-col" style="left:682px;line-height:20px">Partners<br>Gallery<br>Blog<br>About Us<br>Contact Us</div>
<div class="abs foot-col" style="left:768px">Contact Us<ul><li style="color:var(--teal)">Send an Email</li><li style="color:#555">London</li><li>+44 (0) 20 7946 0302</li><li style="color:#555">Sussex</li><li>+44 (0) 1632 960 417</li></ul>
<svg width="30" height="7" style="margin-top:3px"><rect x="0" y="0" width="6" height="6" fill="#009b9d"/><rect x="10" y="0" width="6" height="6" fill="#009b9d"/><rect x="20" y="0" width="6" height="6" fill="#009b9d"/></svg></div>
<div class="abs foot-rule"></div>
<div class="abs foot-base" style="left:375px">Quarling Copyright © 2024. All rights reserved</div>
<div class="abs foot-base" style="left:657px;word-spacing:14px">SITEMAP TERMS&nbsp;OF&nbsp;USE PRIVACY&nbsp;POLICY CONTACT&nbsp;US</div>

</body>
</html>
```